Construction Company Stationary Design

We have previously utilised MakerHive to develop a new logo, we wanted to implement it for a while to ensure we liked it before rolling out new stationary. The time has come and we require:
Business Cards
"With Compliments" Cards
Asset Stickers
Vehicle Stickers
Letterhead
Document Header
Invoice Header
Cover Page
We are an established Construction Company working in Northern Australia (outback) that is venturing into a more corporate environment. We DO NOT do residential construction, we focus on commercial & government (Defence, schools, health etc) and work in both urban and remote environments.
Business Card Requirements:
• Logo
• Company Name
• Staff Name
• Staff Position
• Company Physical & Postal Address
• ABN
• Staff Mobile
• Staff Direct Phone (if applicable)
• Staff Email
• Office Phone
• Office Fax
"With Compliments" cards to be much the same as the business cards but with company details only (no staff details)
Asset stickers again to be much the same but with a space to write in asset number.
Document header requires 4 spaces to enter details much like our previous one attached.
We appreciate that designers time is valuable and would request that samples only be produced for one or two of the required items (say Business Card & Letterhead) and await a feedback score of 4 or more prior to producing the full suite of stationary.
If you require any further information please do not hesitate to contact me. lionel@brevmark.com.au

```html
<!DOCTYPE html>
<html lang="en">
<head>
<meta charset="utf-8">
<title>Corvell Constructions – Business Card</title>
<link href="https://fonts.googleapis.com/css2?family=Source+Sans+3:wght@400;600;700&display=swap" rel="stylesheet">
<style>
  :root {
    --orange: #f15a29;
    --black: #0a0a0a;
    --white: #ffffff;
    --page: #ffffff;
    --edge: #c9c9c9;
  }
  * { margin: 0; padding: 0; box-sizing: border-box; }
  html, body {
    width: 1200px; height: 1059px; overflow: hidden;
    background: var(--page);
    font-family: "Source Sans 3", Arial, sans-serif;
  }
  .canvas { position: relative; width: 1200px; height: 1059px; }

  .card { position: absolute; width: 796px; height: 452px; overflow: hidden; }
  .card-front { left: 36px; top: 45px; background: var(--black); }
  .card-back { left: 385px; top: 590px; background: var(--white); outline: 1px solid var(--edge); }

  .stripes { position: absolute; left: 0; top: 0; width: 796px; height: 452px; }

  .wordmark {
    position: absolute; left: 0; width: 100%;
    text-align: center; font-weight: 700; line-height: 1;
  }
  .wordmark .name { display: block; letter-spacing: 2px; }
  .wordmark .sub { display: block; letter-spacing: 1px; }

  .card-front .wordmark { top: 200px; color: var(--white); }
  .card-front .wordmark .name { font-size: 66px; }
  .card-front .wordmark .sub { font-size: 30px; margin-top: 8px; }

  .card-front .website {
    position: absolute; left: 0; width: 100%; top: 396px;
    text-align: center; color: var(--white); font-size: 22px;
  }
  .website .accent { color: var(--orange); }

  .card-back .wordmark { top: 118px; color: var(--black); }
  .card-back .wordmark .name { font-size: 46px; }
  .card-back .wordmark .sub { font-size: 20px; margin-top: 5px; }

  .contact-panel { position: absolute; left: 0; top: 225px; width: 796px; height: 227px; }

  .staff { position: absolute; left: 42px; top: 244px; color: var(--white); }
  .staff .staff-name { font-size: 29px; line-height: 1; }
  .staff .staff-role { font-size: 19px; line-height: 1; margin-top: 3px; }

  .address {
    position: absolute; left: 42px; top: 373px;
    color: var(--white); font-size: 17px; line-height: 23px;
  }

  .contact-list { position: absolute; left: 378px; top: 266px; list-style: none; }
  .contact-list li {
    display: flex; align-items: center; height: 39.5px;
    color: var(--white); font-size: 17px;
  }
  .contact-list svg { width: 26px; height: 26px; margin-right: 16px; flex: none; }
</style>
</head>
<body>
<div class="canvas">

  <section class="card card-front">
    <svg class="stripes" viewBox="0 0 796 452" aria-hidden="true">
      <polygon points="0,68 290,68 274,92 0,92" fill="var(--orange)"/>
      <polygon points="530,148 796,148 796,174 514,174" fill="var(--orange)"/>
    </svg>
    <div class="wordmark">
      <span class="name">CORVELL</span>
      <span class="sub">CONSTRUCTIONS</span>
    </div>
    <p class="website">www.<span class="accent">corvellbuild</span>.com.au</p>
  </section>

  <section class="card card-back">
    <svg class="stripes" viewBox="0 0 796 452" aria-hidden="true">
      <polygon points="0,43 336,43 328,56 0,56" fill="var(--orange)"/>
      <polygon points="474,89 796,89 796,103 464,103" fill="var(--orange)"/>
    </svg>
    <div class="wordmark">
      <span class="name">CORVELL</span>
      <span class="sub">CONSTRUCTIONS</span>
    </div>

    <svg class="contact-panel" viewBox="0 0 796 227" aria-hidden="true">
      <rect x="0" y="13" width="796" height="214" fill="var(--black)"/>
      <rect x="0" y="0" width="796" height="13" fill="var(--orange)"/>
      <polygon points="0,13 349,13 304,67 0,67" fill="var(--orange)"/>
    </svg>

    <div class="staff">
      <p class="staff-name">Dale Corvell</p>
      <p class="staff-role">Project Manager</p>
    </div>

    <p class="address">14 Ironbark Road<br>Kellin Flats NT 0835</p>

    <ul class="contact-list">
      <li>
        <svg viewBox="0 0 26 26" aria-hidden="true">
          <rect x="7" y="2" width="12" height="22" rx="2" fill="none" stroke="var(--orange)" stroke-width="2"/>
          <rect x="9.5" y="5" width="7" height="12" fill="var(--orange)"/>
          <circle cx="13" cy="20.5" r="1.3" fill="var(--orange)"/>
        </svg>
        0400 318 572
      </li>
      <li>
        <svg viewBox="0 0 26 26" aria-hidden="true">
          <rect x="1" y="6" width="24" height="15" fill="var(--orange)"/>
          <polyline points="1,6 13,15 25,6" fill="none" stroke="var(--black)" stroke-width="1.6"/>
        </svg>
        dale@corvellbuild.com.au
      </li>
      <li>
        <svg viewBox="0 0 26 26" aria-hidden="true">
          <circle cx="13" cy="13" r="11" fill="var(--orange)"/>
          <ellipse cx="13" cy="13" rx="4.5" ry="11" fill="none" stroke="var(--black)" stroke-width="1.3"/>
          <line x1="2" y1="13" x2="24" y2="13" stroke="var(--black)" stroke-width="1.3"/>
          <line x1="4" y1="8" x2="22" y2="8" stroke="var(--black)" stroke-width="1.1"/>
          <line x1="4" y1="18" x2="22" y2="18" stroke="var(--black)" stroke-width="1.1"/>
        </svg>
        www.corvellbuild.com.au
      </li>
      <li>
        <svg viewBox="0 0 26 26" aria-hidden="true">
          <path d="M2 9 Q13 2 24 9 L22 12 L18 11 L18 8 Q13 6 8 8 L8 11 L4 12 Z" fill="var(--orange)"/>
          <path d="M7 13 L19 13 L23 23 L3 23 Z" fill="var(--orange)"/>
          <circle cx="13" cy="18" r="2.6" fill="var(--black)"/>
        </svg>
        (08) 8900 4417
      </li>
    </ul>
  </section>

</div>
</body>
</html>
```